Website Design for Korvinel.com.au (Design + Code)

I am a small business specialising in aquarium monitoring solutions.
Our products essentially are computerised monitoring equipment for aquariums. E.g. https://www.reeflowgauge.com/en-GB/products-shop/marivex-controllers
and also TalMow http://www.talmow.com/
I see the design having 3 pages
* Landing / Home
* Gallery
* Contact us
Design:
I am looking for a cutting edge slick looking site. It should have a number of pages so the site is interactive with contact us, gallery etc.
I have attached our logo and can provide more info as requested. I will be constantly changing the site content as well from my end.
I have attached my logo design which was done via PixelGuild. It can be changed/altered if you feel something else would work better
Final deliverable:
* This project requires both design and development (coding).
* The 3 design pages are to be delivered as PSD files, and the coding as HTML.
The site will need to scale to be viewable on both iPhone/ipads etc as well as standard desktop
Updates
Hi All,
Just based on the couple of designs that have come through so far I would like to specify that for the front landing page, I don't want to be product specific, but rather a page that describes the company and some information about what we do and why it is important to monitor your aquarium. It would still be good to have some images of the monitoring equipment, I will provide or modify the text with the information I am talking about above.
I hope this a little more specific.
Hi All,
While I like the designs that are coming through, I still feel that they are all very template based in look and feel.
I am looking for a unique design that is interactive and engaging to the viewer.
If you need more information from me, please let me know.
Please feel free to submit completely new designs.
Kind Regards,
Rupert
Industry/Entity Type
Small Business

```html
<!DOCTYPE html>
<html lang="en">
<head>
<meta charset="utf-8">
<title>Korvinel – Aquarium Monitoring Solutions</title>
<link href="https://fonts.googleapis.com/css2?family=Varela+Round&family=Open+Sans:wght@400;600;700&display=swap" rel="stylesheet">
<style>
:root{
  --blue:#1a87d0;
  --blue-dark:#1f5fa8;
  --sky-top:#5aaee0;
  --sky-mid:#9fd2f2;
  --ink:#333;
  --muted:#777;
  --line:#ddd;
  --orange:#f79415;
  --orange-dark:#f07a00;
  --footer:#0c0c0c;
  --panel:#f4f4f4;
}
*{margin:0;padding:0;box-sizing:border-box}
html,body{width:905px;height:1200px;overflow:hidden;background:#fff}
body{position:relative;font-family:"Open Sans",Arial,sans-serif;color:var(--ink)}
.abs{position:absolute}
.round{font-family:"Varela Round","Open Sans",sans-serif}

/* header */
.utility{left:616px;top:0;width:206px;height:32px;background:#efefef;clip-path:polygon(0 0,100% 0,94% 100%,6% 100%);
  font-size:10px;color:#555;display:flex;justify-content:center;align-items:center;gap:6px}
.utility span.sep{color:#999}
.brand{left:88px;top:28px;display:flex;align-items:center;gap:8px}
.brand-mark{width:18px;height:18px;background:var(--blue)}
.brand-name{font-family:"Varela Round",sans-serif;font-size:30px;color:#555;line-height:1}
.brand-tag{left:150px;top:75px;font-size:7px;color:var(--blue);letter-spacing:.2px}
.nav{left:362px;top:58px;display:flex;gap:27px;font-size:12px;font-family:"Open Sans",sans-serif;color:#333}
.nav .active{color:var(--blue)}

/* hero */
.hero{left:0;top:97px;width:905px;height:351px;background:linear-gradient(180deg,var(--sky-top) 0%,#8cc8ee 40%,var(--sky-mid) 60%,#6bb7e6 85%,#4aa3dc 100%)}
.hero-title{left:85px;top:186px;font-size:32px;color:#fff}
.hero-sub{left:85px;top:227px;font-size:19px;color:var(--blue-dark)}
.hero-text{left:85px;top:257px;width:300px;font-size:9.6px;line-height:16px;color:#2f5a80}
.dots{left:86px;top:318px;display:flex;gap:3px}
.dots i{width:11px;height:11px;border-radius:50%;background:#111;display:block}
.dots i:first-child{background:#fff}
.hero-frame{left:462px;top:159px;width:356px;height:217px;background:#fff;padding:6px;box-shadow:0 4px 10px rgba(0,0,0,.25)}
.hero-photo{width:100%;height:100%;background:radial-gradient(ellipse at 50% 70%,#3a7fa8 0%,#12408c 50%,#0a2060 100%)}

/* welcome */
.welcome-title{left:0;width:905px;top:478px;text-align:center;font-size:24px;color:#333}
.welcome-text{left:116px;width:664px;top:512px;text-align:center;font-size:9.6px;line-height:14.5px;color:#555}

/* feature cards */
.card-frame{width:231px;height:116px;background:#fff;border:1px solid #ddd;padding:6px;box-shadow:0 1px 3px rgba(0,0,0,.15)}
.card-photo{width:100%;height:100%}
.photo-office{background:linear-gradient(135deg,#d9dde2,#9aa6b2 60%,#5a6672)}
.photo-control{background:linear-gradient(135deg,#2b3d66,#1a2440 60%,#0c1122)}
.card-title{font-size:15.5px;color:var(--blue)}
.card-text{width:230px;font-size:8.8px;line-height:14px;color:#777}
.btn-more{width:89px;height:26px;border-radius:3px;background:linear-gradient(#6ab6e8,#2f88c8);color:#fff;font-size:9.6px;display:flex;align-items:center;justify-content:center}

/* quick contact */
.contact-box{left:594px;top:594px;width:218px;height:235px;border:1px solid #ccc;background:linear-gradient(#fff 70%,#f3f3f3)}
.contact-head{height:40px;border-bottom:1px solid #ddd;background:var(--panel);padding:10px 19px;font-size:17.5px;color:#333}
.field{left:18px;width:185px;height:22px;border:1px solid #ccc;background:#fff;font-size:8.8px;color:#888;padding:5px 8px}
.field.msg{height:50px}
.btn-submit{left:19px;top:197px;width:80px;height:26px;border-radius:2px;background:linear-gradient(#ffa833,var(--orange-dark));color:#fff;font-size:11px;display:flex;align-items:center;justify-content:center}

.divider{left:85px;top:863px;width:736px;height:1px;background:#ddd}

/* blog */
.section-title{font-size:19px;color:#333}
.section-title.orange{color:var(--orange)}
.post-title{left:89px;font-size:12px;color:var(--blue)}
.post-text{left:89px;width:425px;font-size:8.8px;line-height:14.5px;color:#666}

/* gallery */
.thumb{width:80px;height:59px;border:1px solid #ddd;background:#fff;padding:8px}
.thumb div{width:100%;height:100%;background:linear-gradient(135deg,#c4ccd8,#5a6a88)}

/* footer */
.footer{left:0;top:1108px;width:905px;height:92px;background:var(--footer)}
.foot-nav{left:86px;top:1133px;font-size:10.4px;font-weight:600;color:#fff;display:flex;gap:5px}
.copy{left:86px;top:1153px;font-size:9.5px;color:#ccc}
.social{left:700px;top:1132px;display:flex;gap:4px}
.social i{display:block;width:22px;height:22px;border-radius:50%;background:#fff}
</style>
</head>
<body>

<header>
  <div class="abs utility"><span>Register</span><span class="sep">|</span><span>Support</span><span class="sep">|</span><span>Help</span><span class="sep">|</span><span>Store</span></div>
  <div class="abs brand"><span class="brand-mark"></span><span class="brand-name">Korvinel</span></div>
  <div class="abs brand-tag">AQUARIUM MONITORING SOLUTIONS</div>
  <nav class="abs nav"><span class="active">HOME</span><span>ABOUT US</span><span>PRODUCTS</span><span>SERVICES</span><span>GALLERY</span><span>CONTACT</span></nav>
</header>

<section class="abs hero"></section>
<h1 class="abs hero-title round" style="font-weight:400">Aquarium Monitoring</h1>
<h2 class="abs hero-sub round" style="font-weight:400">Duis tincidunt lectus quis dui</h2>
<p class="abs hero-text">Vivamus porttitor purus nisi eleifend libero a tempus libero lectus feugiat felis Morbi diam mauris viverra in gravida eu mattis in ante Morbi eget arcu Morbi porta libero id ullamcorper</p>
<div class="abs dots"><i></i><i></i><i></i><i></i></div>
<div class="abs hero-frame"><div class="hero-photo" role="img" aria-label="Coral reef aquarium with tropical fish"></div></div>

<h2 class="abs welcome-title round" style="font-weight:400">Welcome to Our Website Mainpage</h2>
<p class="abs welcome-text">Duis tincidunt lectus quis dui viverra vestibulum Suspendisse vulputate aliquam dui Nulla elementum dui ut augue Aliquam vehicula mi at mauris Mae-cenas placerat nisl at consequat rhoncus sem nunc gravida justo quis eleifend arcu velit quis lacus&nbsp; Morbi magna magna tincidunt a mattis non imperdiet vitae tellus Sed odio est auctor ac sollicitudin in consequat vitae orci Fusce id felis</p>

<div class="abs card-frame" style="left:84px;top:598px"><div class="card-photo photo-office" role="img" aria-label="Technician working at a monitoring workstation"></div></div>
<h3 class="abs card-title round" style="left:86px;top:724px;font-weight:400">WHY OUR PRODUCT</h3>
<p class="abs card-text" style="left:86px;top:748px">Etiam est nunc venenatis in tristique eu imperdiet ac nisl Cum sociis natoque penatibus et magnis</p>
<div class="abs btn-more" style="left:86px;top:785px">READ MORE</div>

<div class="abs card-frame" style="left:334px;top:598px"><div class="card-photo photo-control" role="img" aria-label="Control room with wall of monitoring screens"></div></div>
<h3 class="abs card-title round" style="left:336px;top:724px;font-weight:400">SERVICES PROVIDE</h3>
<p class="abs card-text" style="left:336px;top:748px">Etiam est nunc venenatis in tristique eu imperdiet ac nisl Cum sociis natoque penatibus et magnis dis</p>
<div class="abs btn-more" style="left:335px;top:785px">READ MORE</div>

<aside class="abs contact-box">
  <div class="contact-head round">Quick Contact</div>
  <div class="abs field" style="top:50px">Your name</div>
  <div class="abs field" style="top:79px">Email address</div>
  <div class="abs field" style="top:108px">Phone no.</div>
  <div class="abs field msg" style="top:137px">Message</div>
  <div class="abs btn-submit">SUBMIT</div>
</aside>

<div class="abs divider"></div>

<h2 class="abs section-title round" style="left:88px;top:890px;font-weight:400">Recent Blog Post</h2>
<h3 class="abs post-title round" style="top:923px;font-weight:400">Integer orci tellus tristique vitae</h3>
<p class="abs post-text" style="top:943px">Mauris vel lacus vitae felis vestibulum volutpat Etiam est nunc venenatis in tristique eu imperdiet ac nisl Cum sociis natoque penatibus et magnis dis</p>
<h3 class="abs post-title round" style="top:988px;font-weight:400">Phasellus felis dolor scelerisque tempus</h3>
<p class="abs post-text" style="top:1008px">Suspendisse vulputate aliquam dui Nulla elementum dui ut augue Aliquam vehicula mi at mauris Maece-nas placerat nisl at consequat rhoncus sem nunc gravida justo quis eleifend arcu</p>

<h2 class="abs section-title orange round" style="left:550px;top:890px;font-weight:400">Our Gallery</h2>
<div class="abs thumb" style="left:553px;top:922px"><div role="img" aria-label="Monitoring controller unit"></div></div>
<div class="abs thumb" style="left:644px;top:922px"><div role="img" aria-label="Controller with display screen"></div></div>
<div class="abs thumb" style="left:733px;top:922px"><div role="img" aria-label="Circuit board and connector parts"></div></div>
<div class="abs thumb" style="left:553px;top:986px"><div role="img" aria-label="Data cable"></div></div>
<div class="abs thumb" style="left:644px;top:986px"><div role="img" aria-label="Controller unit with keypad"></div></div>
<div class="abs thumb" style="left:733px;top:986px"><div role="img" aria-label="Display modules"></div></div>

<footer class="abs footer"></footer>
<nav class="abs foot-nav round"><span>HOME</span><span>|</span><span>ABOUT US</span><span>|</span><span>PRODUCTS</span><span>|</span><span>SERVICES</span><span>|</span><span>GALLERY</span><span>|</span><span>CONTACT</span></nav>
<p class="abs copy">© 2014 Company Name&nbsp; All right reserved&nbsp; Term of Use</p>
<div class="abs social" aria-label="Social links"><i></i><i></i><i></i><i></i></div>

</body>
</html>
```